Elmora Full Spectrum CBD Oil infused with turmeric, black pepper and cacao extracts

Using company logo attached, dosage info attached, PQB disclaimer attached, pharmacist disclaimer below, ingredient list below and bar code.
Above "Full Spectrum" part of the logo I would like "Elmora" in hand written font and in light green color close to the logo color. White background color please. The smaller logos that were attached in the file need to be on the back side of the label with the ingridients list to the right of the logo in and the disclaimers to the left of it.

Requirements
Must have
• -ORGANIC
• -USA GROWN
• -30mL
• -1500MG CBD
• -This product is not approved by PQB for the diagnosis, cure, mitigation, treatment, or prevention of any disease. Please consult with your physician or pharmacist before using CBD if you are taking medication of any kind.
• -Directions: Administer 5 drops sublingually 2-3 times per day or as needed. Hold under your tongue for 60 seconds then swallow.
• -Ingredients: Organic MCT Oil, Organic Hemp Extract, proprietary organic terpene blend, Organic Hemp derived minerals

```html
<!DOCTYPE html>
<html lang="en">
<head>
<meta charset="utf-8">
<title>Elmora Full Spectrum CBD Oil Label</title>
<link rel="stylesheet" href="https://fonts.googleapis.com/css2?family=Great+Vibes&family=Lato:wght@400;700&display=swap">
<style>
  :root {
    --backdrop: #aeb0a6;
    --label-white: #ffffff;
    --pattern-tint: #eef1f4;
    --band-green: #2e8b4f;
    --band-green-light: #3a9a5c;
    --script-green: #8cc63f;
    --ink: #1c1c1c;
    --on-green: #ffffff;
  }
  * { margin: 0; padding: 0; box-sizing: border-box; }
  html, body {
    width: 957px; height: 1200px; overflow: hidden;
    background: var(--backdrop);
    font-family: "Lato", sans-serif;
  }
  .label {
    position: absolute; left: 88px; top: 95px;
    width: 780px; height: 1010px;
    background: var(--label-white);
    overflow: hidden;
  }
  .label-top {
    position: absolute; left: 0; top: 0; width: 100%; height: 506px;
    background: radial-gradient(circle at 50% 45%, var(--label-white) 0%, var(--pattern-tint) 100%);
  }
  .brand-script {
    position: absolute; top: 40px; width: 100%; text-align: center;
    font-family: "Great Vibes", cursive; font-size: 60px; color: var(--script-green);
    line-height: 1;
  }
  .product-line {
    position: absolute; top: 118px; width: 100%; text-align: center;
    font-family: "Lato", sans-serif;
    font-size: 48px; color: var(--ink); letter-spacing: 0.5px;
  }
  .brand-mark {
    position: absolute; top: 270px; width: 100%;
    display: flex; justify-content: center; align-items: center; gap: 16px;
  }
  .brand-mark .dot {
    width: 40px; height: 40px; border-radius: 50%; background: var(--band-green);
  }
  .brand-mark .name {
    font-family: "Lato", sans-serif;
    font-size: 48px; color: var(--band-green); font-weight: 400;
  }
  .tagline {
    position: absolute; top: 426px; width: 100%; text-align: center;
    font-family: "Lato", sans-serif;
    font-size: 40px; color: var(--ink);
  }
  .label-band {
    position: absolute; left: 0; top: 506px; width: 100%; height: 504px;
    background: linear-gradient(90deg, var(--band-green) 0%, var(--band-green-light) 50%, var(--band-green) 100%);
    color: var(--on-green);
    font-family: "Lato", sans-serif;
  }
  .organic-box {
    position: absolute; left: 79px; top: 33px; width: 621px; height: 84px;
    border: 4px solid var(--on-green);
    display: flex; align-items: center; justify-content: center;
    font-size: 48px;
  }
  .facts {
    position: absolute; left: 0; top: 209px; width: 100%; height: 161px;
  }
  .disclaimer {
    position: absolute; left: 45px; top: 6px; width: 190px;
    font-size: 24px; line-height: 1.35;
  }
  .divider {
    position: absolute; top: 0; width: 4px; height: 161px; background: var(--on-green);
  }
  .divider.first { left: 249px; }
  .divider.second { left: 532px; }
  .fact {
    position: absolute; top: 55px; font-size: 33px; white-space: nowrap;
  }
  .fact.grown { left: 253px; width: 279px; text-align: center; }
  .fact.dose { left: 536px; width: 244px; text-align: center; top: 45px; }
  .volume {
    position: absolute; left: 306px; top: 436px; width: 160px; height: 54px;
    background: var(--label-white); color: var(--ink);
    display: flex; align-items: center; justify-content: center;
    font-family: "Lato", sans-serif;
    font-size: 30px;
  }
</style>
</head>
<body>
  <section class="label">
    <div class="label-top" role="img" aria-label="Light water droplet texture across the white label area">
      <div class="brand-script">Elmora</div>
      <div class="product-line">FULL SPECTRUM</div>
      <div class="brand-mark">
        <span class="dot"></span>
        <span class="name">Elmora</span>
      </div>
      <div class="tagline">HOLISTIC HEALING</div>
    </div>
    <div class="label-band">
      <div class="organic-box">ORGANIC HEMP</div>
      <div class="facts">
        <p class="disclaimer">cure, mitigation,<br>treatment, or<br>prevention of<br>any disease</p>
        <span class="divider first"></span>
        <p class="fact grown">USA GROWN</p>
        <span class="divider second"></span>
        <p class="fact dose">1500MG CBD</p>
      </div>
      <div class="volume">30mL</div>
    </div>
  </section>
</body>
</html>
```